Best local air conditioning and heating contractor

We need a website design for a new company in Tampa Bay called the Brightwell Cooling Company. We provide superior services for residential and commercial properties as well as maintenance and installing HVAC systems. We also want to sell equipment, parts and filter on the website as well. We want it easy to use for customers. Rich with content and keywords for our area.

Target Market(s)

homeowners in Tampa Bay

Industry/Entity Type

HVAC air conditioning and heating

Coding

Coded - Design and coding required

Number of Pages Required

5+ page

Font styles to use
Sans Serif

Requirements
Nice to have
• would like the colors to be same as logo

```html
<!DOCTYPE html>
<html lang="en">
<head>
<meta charset="utf-8">
<title>Brightwell Cooling Company – Heating and Air Conditioning</title>
<link href="https://fonts.googleapis.com/css2?family=Poppins:wght@400;500;600;700;800&display=swap" rel="stylesheet">
<style>
:root{
  --navy:#1c3466;
  --navy-deep:#16295a;
  --blue:#1d4f96;
  --footer:#0d1a3c;
  --red:#d7262e;
  --ink:#1e1e1e;
  --muted:#6b6b6b;
  --light:#f3f3f3;
  --line:#e3e3e3;
  --white:#fff;
}
*{box-sizing:border-box;margin:0;padding:0}
html,body{width:1200px;height:4428px;overflow:hidden}
body{font-family:"Poppins",Arial,sans-serif;color:var(--ink);background:var(--white);position:relative}
a{color:inherit;text-decoration:none}
.abs{position:absolute}
.photo{position:absolute}
.btn{position:absolute;background:var(--red);color:var(--white);font-weight:600;font-size:13px;display:flex;align-items:center;justify-content:center;letter-spacing:.5px;border-radius:2px}

/* top bar */
.topbar{position:absolute;left:0;top:0;width:1200px;height:40px;background:var(--navy-deep);color:var(--white);font-size:13px;display:flex;align-items:center;padding:0 60px;gap:28px}
.topbar .item{display:flex;align-items:center;gap:8px}
.topbar .social{margin-left:auto;display:flex;gap:10px}
.dot{width:14px;height:14px;border-radius:50%;background:var(--white);display:inline-block}

/* nav */
.nav{position:absolute;left:0;top:40px;width:1200px;height:104px;background:var(--white);font-size:15px;font-weight:600}
.nav a{position:absolute;top:42px}
.nav a.active{color:var(--red)}
.nav a.active::after{content:"";position:absolute;left:0;right:0;bottom:-8px;height:3px;background:var(--red)}
.brand{position:absolute;left:462px;top:44px;width:276px;height:126px;background:var(--white);z-index:3;display:flex;align-items:center;justify-content:center;gap:10px;border-radius:0 0 6px 6px}
.brand .mark{width:18px;height:18px;background:var(--red)}
.brand span{font-weight:800;color:var(--navy);font-size:19px;line-height:1.15;text-transform:uppercase;width:200px}

/* hero */
.hero{position:absolute;left:0;top:144px;width:1200px;height:448px;background:linear-gradient(180deg,#3d5a7a 0%,#27405f 60%,#1c2f48 100%)}
.hero h1{position:absolute;top:120px;width:100%;text-align:center;color:var(--white);font-size:50px;font-weight:700;line-height:1.15}
.hero p{position:absolute;top:250px;left:370px;width:460px;text-align:center;color:var(--white);font-size:21px;line-height:1.3}

/* feature cards */
.band-light{position:absolute;left:0;top:592px;width:1200px;height:120px;background:var(--light)}
.feature{position:absolute;top:652px;width:300px;height:160px;background:var(--white);border-radius:8px;box-shadow:0 6px 20px rgba(0,0,0,.12);padding:26px 28px}
.feature svg{display:block}
.feature h3{color:var(--navy);font-size:15px;font-weight:600;margin-top:8px}
.feature p{font-size:9px;color:var(--muted);line-height:1.3;margin-top:4px;width:150px}
.more{position:absolute;right:28px;bottom:18px;font-size:11px;font-weight:700;color:var(--red);display:flex;align-items:center;gap:8px}

/* about panels */
.panel{position:absolute;background:var(--white);box-shadow:0 6px 24px rgba(0,0,0,.12);padding:40px 44px}
.panel h2{font-size:34px;font-weight:700;color:var(--ink);line-height:1}
.panel p{font-size:14px;color:var(--muted);line-height:1.45;margin-top:18px}
.panel .btn{position:static;width:180px;height:44px;margin-top:24px}

/* services */
.services{position:absolute;left:0;top:1972px;width:1200px;height:680px;background:linear-gradient(180deg,#1f4d93,#173f7c)}
.h-section{position:absolute;width:100%;text-align:center;font-size:28px;font-weight:700}
.svc{position:absolute;top:2140px;width:260px;height:340px;background:var(--white);border-radius:10px;overflow:hidden}
.svc .img{position:absolute;left:10px;top:10px;width:240px;height:140px;border-radius:6px}
.svc .icon{position:absolute;left:22px;top:126px;width:48px;height:48px;border-radius:50%;background:var(--red);border:3px solid var(--white);display:flex;align-items:center;justify-content:center}
.svc h3{position:absolute;left:22px;top:186px;font-size:15px;font-weight:700}
.svc p{position:absolute;left:22px;top:212px;width:216px;font-size:10px;line-height:1.35;color:var(--muted)}
.svc .more{left:22px;right:auto}

/* products */
.prod-bg{position:absolute;top:2876px;width:232px;height:232px;background:#ececec;border-radius:26px}
.prod{position:absolute;top:2890px;width:176px;height:220px;background:var(--white);border-radius:6px;box-shadow:0 4px 14px rgba(0,0,0,.1);text-align:center}
.prod .img{position:absolute;left:44px;top:14px;width:88px;height:88px;border-radius:8px}
.prod h4{position:absolute;top:118px;width:100%;font-size:12px;font-weight:600}
.prod .price{position:absolute;top:138px;width:100%;font-size:22px;font-weight:700;color:var(--red)}
.prod .price s{color:#555;font-size:17px;font-weight:500}
.prod .btn{left:54px;top:180px;width:68px;height:20px;font-size:8px}

/* contact */
.contact-band{position:absolute;left:0;top:3312px;width:1200px;height:608px;background:var(--light)}
.form{position:absolute;left:112px;top:3492px;width:580px;height:408px;background:var(--white);padding:34px 44px}
.form h2{font-size:30px;font-weight:700}
.field{position:absolute;height:36px;background:#ececec;font-size:12px;padding:10px 12px;color:#333}

/* footer */
.footer{position:absolute;left:0;top:3960px;width:1200px;height:468px;background:var(--footer);color:#c9d0e4}
.fcol{position:absolute;top:56px}
.fcol h5{color:var(--white);font-size:16px;font-weight:600;letter-spacing:.5px}
.fcol h5::after{content:"";display:block;width:36px;height:3px;background:var(--red);margin-top:12px}
.footer p{font-size:13px;line-height:1.8}
.crow{display:flex;gap:14px;margin-top:20px;font-size:13px}
.crow b{color:var(--white);font-weight:600;display:block}
.qlist li{list-style:none;display:flex;justify-content:space-between;width:240px;font-size:13px;padding:10px 0}
.hours div{margin-top:18px;font-size:13px}
.hours b{color:var(--white);font-weight:600;display:block}
.fsocial{display:flex;gap:12px;margin-top:26px}
.fsocial span{width:36px;height:36px;border-radius:50%;background:var(--blue);display:flex;align-items:center;justify-content:center}
</style>
</head>
<body>

<header class="topbar">
  <span class="item"><svg width="14" height="11" viewBox="0 0 14 11"><rect x=".5" y=".5" width="13" height="10" fill="none" stroke="#fff"/><path d="M1 1l6 5 6-5" fill="none" stroke="#fff"/></svg>hello@brightwellcooling.com</span>
  <span class="item"><svg width="12" height="12" viewBox="0 0 24 24"><path fill="#fff" d="M6.6 10.8a15 15 0 006.6 6.6l2.2-2.2a1 1 0 011-.3 11 11 0 003.6.6 1 1 0 011 1V20a1 1 0 01-1 1A17 17 0 013 4a1 1 0 011-1h3.5a1 1 0 011 1 11 11 0 00.6 3.6 1 1 0 01-.3 1z"/></svg>(123) 456 7890</span>
  <span class="social"><i class="dot"></i><i class="dot"></i><i class="dot"></i></span>
</header>

<nav class="nav">
  <a class="active" style="left:60px">HOME</a>
  <a style="left:172px">ABOUT</a>
  <a style="left:300px">SERVICES</a>
  <a style="left:760px">PRODUCTS</a>
  <a style="left:900px">FINANCING</a>
  <a style="left:1084px">BLOG</a>
</nav>
<div class="brand"><i class="mark"></i><span>Brightwell Cooling Company</span></div>

<section class="hero" role="img" aria-label="Evening city waterfront skyline behind a dark overlay">
  <h1>HEATING AND AIR<br>CONDITIONING SERVICES</h1>
  <p>Lorem ipsum dolor sit amet, consectetuer adipiscing elit. Aenean commodo ligula eget dolor. Aenean massa.</p>
  <a class="btn" style="left:450px;top:364px;width:300px;height:56px;font-size:16px">CALL US NOW : (123) 456 7890</a>
</section>

<div class="band-light"></div>
<article class="feature" style="left:132px">
  <svg width="40" height="40" viewBox="0 0 40 40" fill="none" stroke="#1c3466" stroke-width="2"><path d="M6 36h28M10 36V14l10-8 10 8v22M16 36v-10h8v10"/></svg>
  <h3>Heating</h3><p>Reliable furnace repair and heat pump care for your home.</p>
  <span class="more">READ MORE <svg width="22" height="10" viewBox="0 0 22 10"><path d="M0 5h20M15 1l5 4-5 4" stroke="#d7262e" stroke-width="2" fill="none"/></svg></span>
</article>
<article class="feature" style="left:450px">
  <svg width="40" height="40" viewBox="0 0 40 40" fill="none" stroke="#1c3466" stroke-width="2"><rect x="4" y="8" width="32" height="16" rx="2"/><path d="M8 18h24M12 30v4M20 30v6M28 30v4"/></svg>
  <h3>Cooling</h3><p>Fast AC tune ups and repairs to keep every room cool.</p>
  <span class="more">READ MORE <svg width="22" height="10" viewBox="0 0 22 10"><path d="M0 5h20M15 1l5 4-5 4" stroke="#d7262e" stroke-width="2" fill="none"/></svg></span>
</article>
<article class="feature" style="left:816px">
  <svg width="40" height="40" viewBox="0 0 40 40" fill="none" stroke="#1c3466" stroke-width="2"><path d="M8 32L24 16M22 8a6 6 0 008 8l2 2-4 4-2-2a6 6 0 00-8-8zM8 8l8 8M6 10l4-4M24 24l8 8"/></svg>
  <h3>Repairs</h3><p>Same day service calls for all makes of HVAC systems.</p>
  <span class="more">READ MORE <svg width="22" height="10" viewBox="0 0 22 10"><path d="M0 5h20M15 1l5 4-5 4" stroke="#d7262e" stroke-width="2" fill="none"/></svg></span>
</article>

<div class="photo" style="left:72px;top:944px;width:496px;height:372px;background:linear-gradient(135deg,#c9a27a,#8a6a4e 55%,#5a4a3e)" role="img" aria-label="HVAC technician in a cap smiling on the job"></div>
<section class="panel" style="left:520px;top:1040px;width:608px;height:360px">
  <h2>WHO WE ARE</h2>
  <p>Many homeowners struggle to find an HVAC team they can trust. We listen first, explain clearly and price fairly, so your heating and cooling system works when you need it most. Our local crew brings years of training to every visit and stands behind every job we complete.</p>
  <a class="btn">MORE ABOUT US</a>
</section>

<div class="photo" style="left:768px;top:1508px;width:300px;height:368px;background:linear-gradient(135deg,#d9dde2,#9aa3ad 60%,#6e7782)" role="img" aria-label="Two technicians installing ceiling ductwork"></div>
<section class="panel" style="left:72px;top:1580px;width:700px;height:340px">
  <h2>WHAT WE DO</h2>
  <p>We install, repair and maintain heating and air conditioning systems for homes and businesses across the bay area. From new equipment and duct work to filters and seasonal tune ups, we keep your indoor air clean, comfortable and efficient all year long.</p>
  <a class="btn">CONTACT US NOW</a>
</section>

<section class="services" role="img" aria-label="Blue tinted background of outdoor condenser units"></section>
<h2 class="h-section" style="top:2036px;color:#fff">OUR SERVICES</h2>
<article class="svc" style="left:132px">
  <div class="img" style="background:linear-gradient(135deg,#b88a6a,#6d5346)" role="img" aria-label="Hands fitting a gas line"></div>
  <span class="icon"><svg width="22" height="22" viewBox="0 0 24 24" fill="none" stroke="#fff" stroke-width="2"><path d="M12 3c3 4 5 6 5 10a5 5 0 01-10 0c0-3 2-5 5-10z"/></svg></span>
  <h3>GAS FITTING</h3><p>Safe gas line installs and checks for furnaces, water heaters and ranges, done by licensed techs who test every joint before leaving.</p>
  <span class="more">READ MORE <svg width="12" height="12"><circle cx="6" cy="6" r="6" fill="#d7262e"/></svg></span>
</article>
<article class="svc" style="left:470px">
  <div class="img" style="background:linear-gradient(135deg,#c78a50,#7a5236)" role="img" aria-label="Copper pipe fittings being joined"></div>
  <span class="icon"><svg width="22" height="22" viewBox="0 0 24 24" fill="none" stroke="#fff" stroke-width="2"><path d="M3 8h10v8h8M3 12h6"/></svg></span>
  <h3>PIPE FITTING</h3><p>Refrigerant and condensate lines sized and fitted right, so your system runs quietly, drains well and lasts for many years.</p>
  <span class="more">READ MORE <svg width="12" height="12"><circle cx="6" cy="6" r="6" fill="#d7262e"/></svg></span>
</article>
<article class="svc" style="left:808px">
  <div class="img" style="background:linear-gradient(135deg,#b9c0c8,#6f7884)" role="img" aria-label="New outdoor AC units on a wall"></div>
  <span class="icon"><svg width="22" height="22" viewBox="0 0 24 24" fill="none" stroke="#fff" stroke-width="2"><rect x="4" y="5" width="16" height="14"/><circle cx="12" cy="12" r="4"/></svg></span>
  <h3>NEW INSTALLS</h3><p>High efficiency systems matched to your home, with clean installs, clear pricing and financing options that fit your budget.</p>
  <span class="more">READ MORE <svg width="12" height="12"><circle cx="6" cy="6" r="6" fill="#d7262e"/></svg></span>
</article>
<a class="btn" style="left:508px;top:2556px;width:184px;height:48px">VIEW ALL SERVICES</a>

<h2 class="h-section" style="top:2736px">OUR BEST SELLING PRODUCTS</h2>
<div class="prod-bg" style="left:80px"></div><div class="prod-bg" style="left:356px"></div><div class="prod-bg" style="left:632px"></div><div class="prod-bg" style="left:908px"></div>
<article class="prod" style="left:108px"><div class="img" style="background:radial-gradient(circle,#d6d6d6,#8d8d8d)" role="img" aria-label="Blower fan motor"></div><h4>Product Title</h4><div class="price">$100 <s>$150</s></div><a class="btn">BUY NOW</a></article>
<article class="prod" style="left:384px"><div class="img" style="background:radial-gradient(circle,#5a4a44,#1e1a1a)" role="img" aria-label="Run capacitor"></div><h4>Product Title</h4><div class="price">$100 <s>$150</s></div><a class="btn">BUY NOW</a></article>
<article class="prod" style="left:660px"><div class="img" style="background:radial-gradient(circle,#fff 40%,#444 42%,#fff 60%)" role="img" aria-label="Coiled drive belt"></div><h4>Product Title</h4><div class="price">$100 <s>$150</s></div><a class="btn">BUY NOW</a></article>
<article class="prod" style="left:936px"><div class="img" style="background:radial-gradient(circle,#fff 40%,#333 42%,#fff 58%)" role="img" aria-label="Rubber belt loop"></div><h4>Product Title</h4><div class="price">$100 <s>$150</s></div><a class="btn">BUY NOW</a></article>

<div class="contact-band"></div>
<div class="photo" style="left:840px;top:3420px;width:264px;height:440px;background:linear-gradient(135deg,#c0a68a,#6b5a4e 60%,#3d3633)" role="img" aria-label="Technician working on an indoor unit"></div>
<section class="form">
  <h2>CONTACT US NOW</h2>
  <div class="field" style="left:44px;top:90px;width:240px">Name</div>
  <div class="field" style="left:300px;top:90px;width:236px">Email</div>
  <div class="field" style="left:44px;top:140px;width:240px">Phone</div>
  <div class="field" style="left:300px;top:140px;width:236px">Service</div>
  <div class="field" style="left:44px;top:190px;width:492px;height:120px">Message</div>
  <a class="btn" style="left:176px;top:340px;width:228px;height:44px;font-size:11px">REQUEST A QUOTE NOW</a>
</section>

<footer class="footer">
  <div class="fcol" style="left:28px;width:250px">
    <h5>ABOUT US</h5>
    <p style="margin-top:24px">We are an award winning HVAC company with over 20 years of experience in the business. We provide a wide range of services for both residential and commercial clients.</p>
    <div class="fsocial"><span><i class="dot"></i></span><span><i class="dot"></i></span><span><i class="dot"></i></span></div>
  </div>
  <div class="fcol" style="left:340px;width:240px">
    <h5>CONTACT US</h5>
    <div class="crow"><svg width="16" height="20" viewBox="0 0 16 20"><path d="M8 0a7 7 0 017 7c0 5-7 13-7 13S1 12 1 7a7 7 0 017-7z" fill="#fff"/></svg><span><b>Address:</b>418 Harbor Lane, Tampa, FL</span></div>
    <div class="crow"><svg width="16" height="16" viewBox="0 0 24 24"><path fill="#fff" d="M6.6 10.8a15 15 0 006.6 6.6l2.2-2.2a1 1 0 011-.3 11 11 0 003.6.6 1 1 0 011 1V20a1 1 0 01-1 1A17 17 0 013 4a1 1 0 011-1h3.5a1 1 0 011 1 11 11 0 00.6 3.6 1 1 0 01-.3 1z"/></svg><span><b>Phone:</b>+1 813 555 0142</span></div>
    <div class="crow"><svg width="16" height="16" viewBox="0 0 16 16"><rect x="4" y="0" width="8" height="16" rx="2" fill="#fff"/></svg><span><b>Mobile:</b>+1 813 555 0143</span></div>
    <div class="crow"><svg width="16" height="12" viewBox="0 0 14 11"><rect x=".5" y=".5" width="13" height="10" fill="none" stroke="#fff"/><path d="M1 1l6 5 6-5" fill="none" stroke="#fff"/></svg><span><b>Email:</b>support@brightwellcooling.com</span></div>
  </div>
  <div class="fcol" style="left:652px">
    <h5>QUICK LINKS</h5>
    <ul class="qlist" style="margin-top:14px"><li>About<span>›</span></li><li>Contact<span>›</span></li><li>News List<span>›</span></li><li>Services<span>›</span></li><li>Shop<span>›</span></li></ul>
  </div>
  <div class="fcol hours" style="left:964px;width:210px">
    <h5>OPENING HOURS</h5>
    <div><b>Monday - Friday</b>8:00 AM - 5:00 PM</div>
    <div><b>Saturday</b>9:00 AM - 4:00 PM</div>
    <div><b>Sunday</b>CLOSED</div>
  </div>
</footer>

</body>
</html>
```